Bref créative
Marisela Quarn Insurance biz card
biz card and stationary
Bright & Fun-filled
Marisela Quarn
Independent Agent
Charlotte, NC
mquarn@brookvantnet.example
please use the headshot and the logo that are attached.
please use the content of the back of the card we have included.
headshot
logo
card back

```html
<!DOCTYPE html>
<html lang="en">
<head>
<meta charset="utf-8">
<title>Marisela Quarn Insurance – Business Card</title>
<link rel="stylesheet" href="https://fonts.googleapis.com/css2?family=Lora:wght@400;600;700&display=swap">
<style>
  :root {
    --page-bg: #e9ebee;
    --blue-deep: #0b4f93;
    --blue-mid: #1f7bc8;
    --blue-light: #5fb3ea;
    --orange: #f39a1e;
    --white: #ffffff;
    --ink-soft: #d9ecfb;
  }
  * { box-sizing: border-box; margin: 0; padding: 0; }
  html, body { width: 1200px; height: 901px; overflow: hidden; }
  body {
    background: var(--page-bg);
    font-family: "Lora", Georgia, serif;
    position: relative;
  }
  .card {
    position: absolute;
    left: 250px;
    width: 700px;
    height: 400px;
    border-radius: 22px;
    overflow: hidden;
    box-shadow: 0 6px 18px rgba(0,0,0,.18);
  }
  .card-back { top: 33px; background: linear-gradient(160deg, var(--blue-light) 0%, var(--blue-mid) 45%, var(--blue-deep) 100%); }
  .card-front { top: 468px; background: var(--white); }

  /* back */
  .services { position: absolute; left: 46px; top: 70px; color: var(--white); }
  .services-title { font-size: 22px; font-weight: 600; margin-bottom: 14px; }
  .services-list { list-style: none; font-size: 19px; line-height: 1.65; }
  .services-list li { padding-left: 26px; position: relative; }
  .services-list li::before {
    content: ""; position: absolute; left: 4px; top: 12px;
    width: 8px; height: 8px; border-radius: 50%; background: var(--white);
  }
  .back-glow {
    position: absolute; right: -60px; top: -80px; width: 360px; height: 360px;
    border-radius: 50%; background: radial-gradient(circle, rgba(255,255,255,.28), rgba(255,255,255,0) 70%);
  }

  /* front */
  .front-waves { position: absolute; inset: 0; }
  .brand {
    position: absolute; left: 0; right: 0; top: 120px;
    display: flex; justify-content: center; align-items: center; gap: 16px;
  }
  .brand-mark {
    width: 40px; height: 40px; border-radius: 50%;
    background: var(--blue-deep); flex: none;
  }
  .brand-name {
    font-size: 36px; font-weight: 600; color: var(--blue-deep);
    white-space: nowrap;
  }
  .agent { position: absolute; left: 56px; top: 300px; color: var(--white); }
  .agent-name { font-size: 26px; font-weight: 700; }
  .agent-role { font-size: 17px; margin-top: 8px; color: var(--ink-soft); }
  .divider { position: absolute; left: 352px; top: 298px; width: 2px; height: 72px; background: rgba(255,255,255,.7); }
  .contact { position: absolute; left: 376px; top: 302px; color: var(--white); font-size: 16px; list-style: none; }
  .contact li { display: flex; align-items: center; gap: 10px; margin-bottom: 16px; white-space: nowrap; }
  .contact svg { width: 18px; height: 18px; fill: var(--white); flex: none; }
</style>
</head>
<body>

<section class="card card-back" aria-label="Card back">
  <div class="back-glow"></div>
  <div class="services">
    <p class="services-title">I can also help you with......</p>
    <ul class="services-list">
      <li>Medicare Advantage Plans</li>
      <li>Long Term Care Insurance</li>
      <li>Fixed Annuities</li>
      <li>Life Insurance</li>
      <li>Medicare Supplement Insurance</li>
      <li>Individual Major Medical Insurance</li>
    </ul>
  </div>
</section>

<section class="card card-front" aria-label="Card front">
  <svg class="front-waves" viewBox="0 0 700 400" preserveAspectRatio="none" aria-hidden="true">
    <defs>
      <linearGradient id="frontBand" x1="0" y1="0" x2="0" y2="1">
        <stop offset="0" stop-color="#3a98dc"/>
        <stop offset="1" stop-color="#0b4f93"/>
      </linearGradient>
    </defs>
    <path d="M0 262 C180 236 430 250 700 196 L700 400 L0 400 Z" fill="url(#frontBand)"/>
    <path d="M0 250 C190 226 430 240 700 184" fill="none" stroke="#f39a1e" stroke-width="4"/>
    <path d="M0 256 C185 232 430 246 700 190" fill="none" stroke="#8ec9f0" stroke-width="3"/>
  </svg>

  <div class="brand">
    <span class="brand-mark"></span>
    <span class="brand-name">Marisela Quarn Insurance</span>
  </div>

  <div class="agent">
    <p class="agent-name">Marisela Quarn</p>
    <p class="agent-role">Independent Agent</p>
  </div>
  <div class="divider"></div>
  <ul class="contact">
    <li>
      <svg viewBox="0 0 24 24"><path d="M6.6 10.8a15.1 15.1 0 0 0 6.6 6.6l2.2-2.2a1 1 0 0 1 1-.25 11.4 11.4 0 0 0 3.6.57 1 1 0 0 1 1 1V20a1 1 0 0 1-1 1A17 17 0 0 1 3 4a1 1 0 0 1 1-1h3.5a1 1 0 0 1 1 1c0 1.25.2 2.45.57 3.57a1 1 0 0 1-.25 1z"/></svg>
      704-555-0147
    </li>
    <li>
      <svg viewBox="0 0 24 24"><path d="M3 5h18v14H3z M3 5l9 7 9-7" fill="none" stroke="#fff" stroke-width="2"/></svg>
      mquarn@brookvantnet.example
    </li>
  </ul>
</section>

</body>
</html>
```